South Carolina Bridal and Formal Wear Store

We want The Gown Parlor of Ashcombe website to feel luxurious, elegant, welcoming, and approachable—without feeling overpriced or intimidating. The site should immediately show that we are a full-service bridal and formal wear destination, offering bridal gowns, prom, mothers’ dresses, tuxedos and suits, accessories, and more. We want beautiful, high-end imagery and a clean, modern design while still reflecting the warm, personal experience customers receive when they walk into our boutique. Most importantly, the website should be easy to shop and navigate, allowing customers to browse our collections, see what we offer, understand price ranges, book appointments, and feel excited and comfortable choosing The Gown Parlor of Ashcombe for all of their special-event needs.

Target Market(s)

Women ages 18-50. Brides, engaged women, mothers of the occasion

Industry/Entity Type

Bridal and Formal Wear

Coding

Coded - Design and coding required

Number of Pages Required

5+ page

Font styles to use
Sans Serif

Colors

Designer to choose colors to be used in the design.

Requirements
Must have
• Appointment area, about us staff area, what we offer and designers our logo
Nice to have
• Modern Southern Luxury: Clean, elegant, and upscale with soft neutral tones, beautiful bridal photography, and a warm Lowcountry feel.
Should not have
• pricing

```html
<!DOCTYPE html>
<html lang="en">
<head>
<meta charset="utf-8">
<title>The Gown Parlor of Ashcombe — Pages</title>
<link href="https://fonts.googleapis.com/css2?family=Inter:wght@400;500;600;700&family=Playfair+Display:wght@400;500&display=swap" rel="stylesheet">
<style>
:root{
  --espresso:#2c1a12;
  --ink:#33241d;
  --muted:#8a7870;
  --rose:#c48f84;
  --blush:#f6e8e4;
  --sand:#f3ece7;
  --cream:#faf8f6;
  --line:#eee6e1;
  --white:#ffffff;
  --footer-text:#bba99f;
}
*{box-sizing:border-box;margin:0;padding:0}
html,body{width:1200px;height:1200px;overflow:hidden;background:var(--white)}
body{font-family:"Inter",Arial,sans-serif;color:var(--ink)}
.stage{position:absolute;left:0;top:0;width:1920px;height:1920px;transform:scale(.625);transform-origin:0 0}
.page{position:absolute;top:50px;width:611px;background:var(--white)}
.page--designers{left:30px}
.page--appointments{left:660px}
.page--faq{left:1291px}

/* header */
.site-header{height:57px;display:flex;align-items:center;justify-content:space-between;padding:0 34px 0 36px}
.brand{font-family:"Playfair Display",Georgia,serif;font-size:11px;line-height:12px;color:var(--espresso);white-space:nowrap}
.nav{display:flex;align-items:center;gap:14px;font-size:6.3px;color:var(--ink)}
.nav a{color:inherit;text-decoration:none;padding:3px 0}
.nav a.is-active{border-bottom:1px solid var(--rose)}
.btn-book{background:var(--espresso);color:var(--white);border-radius:10px;padding:6px 11px;font-weight:600;font-size:6px;margin-left:3px;box-shadow:0 2px 4px rgba(0,0,0,.15)}

/* body */
.page-body{background:var(--cream);padding:18px 45px 0}
.page-title{font-family:"Playfair Display",Georgia,serif;font-weight:400;font-size:22px;text-align:center;color:var(--ink);line-height:28px}
.page-lead{font-size:7.4px;line-height:15px;color:#9b7d70;text-align:center;max-width:330px;margin:6px auto 0}
.section-title{font-family:"Playfair Display",Georgia,serif;font-weight:400;font-size:16px;text-align:center;color:var(--ink)}

/* designers */
.page--designers .page-body{height:347px}
.designer-grid{display:grid;grid-template-columns:repeat(4,122px);gap:11px;margin-top:27px}
.designer-card{height:52px;background:var(--white);border-radius:5px;box-shadow:0 1px 5px rgba(60,30,20,.08);display:flex;flex-direction:column;align-items:center;justify-content:center;gap:4px}
.designer-name{font-size:7px;font-weight:600}
.designer-type{font-size:4.6px;letter-spacing:.6px;text-transform:uppercase;color:#a8958c}
.designer-note{font-size:5.6px;color:var(--muted);text-align:center;margin-top:16px}

/* appointments */
.page--appointments .page-body{height:1396px}
.experience-heading{margin-top:30px}
.experience-grid{display:grid;grid-template-columns:252px 252px;grid-template-rows:365px 114px 102px 102px;column-gap:16px;row-gap:16px;margin-top:17px}
.experience-card{background:var(--white);border-radius:6px;box-shadow:0 1px 6px rgba(60,30,20,.08);padding:14px 13px}
.experience-name{font-size:8px;font-weight:600;display:flex;align-items:center;gap:6px}
.badge{background:var(--rose);color:var(--white);font-size:4.6px;font-weight:600;padding:2px 5px;border-radius:6px}
.experience-meta{font-size:5.3px;color:var(--rose);margin-top:5px}
.experience-desc{font-size:6.2px;line-height:11.8px;color:var(--muted);margin-top:6px}
.fee{display:inline-block;background:var(--sand);font-size:5px;font-weight:600;padding:3px 6px;border-radius:8px;margin-top:6px;color:var(--ink)}
.vip-box{background:var(--blush);border-left:2px solid var(--rose);border-radius:6px;padding:9px 13px;margin-top:8px}
.vip-box h4{font-size:6px;font-weight:600;color:#8c5a50;margin-bottom:6px}
.vip-list{list-style:none}
.vip-list li{font-size:5.6px;line-height:9px;color:#5a4038;padding-left:9px;position:relative;margin-bottom:5px}
.vip-list li::before{content:"+";position:absolute;left:0;color:var(--rose)}
.fine-print{font-size:4.8px;line-height:8.2px;color:var(--muted);margin-top:6px}
.fee b{font-weight:700}
.fee span{font-weight:400;color:var(--muted)}

.request-heading{margin-top:55px}
.request-lead{font-size:6.5px;line-height:10.5px;color:var(--muted);text-align:center;max-width:260px;margin:2px auto 0}
.request-layout{display:grid;grid-template-columns:248px 245px;justify-content:space-between;margin-top:14px}
.experience-awaits h3{font-family:"Playfair Display",Georgia,serif;font-weight:400;font-size:16px;margin-top:6px}
.experience-awaits p{font-size:6.3px;line-height:13px;color:var(--muted);margin-top:8px}
.perks{list-style:none;margin-top:8px}
.perks li{font-size:6.3px;line-height:16.5px;padding-left:10px;position:relative}
.perks li::before{content:"+";position:absolute;left:0;color:var(--rose)}
.callout{background:var(--blush);border-left:2px solid var(--rose);border-radius:5px;padding:9px 12px;margin-top:10px;font-size:6px;line-height:12px;color:#5a4038}
.callout b{font-weight:700;color:var(--ink)}

.request-form{background:var(--white);border-radius:7px;box-shadow:0 1px 6px rgba(60,30,20,.08);padding:16px;height:359px}
.request-form h4{font-size:8px;font-weight:600;margin-bottom:12px}
.field{margin-bottom:9px}
.field label{display:block;font-size:5px;font-weight:500;margin-bottom:4px}
.input{height:19px;background:#f7f3f0;border:1px solid var(--line);border-radius:4px;font-size:5.6px;color:#a99a92;padding:0 8px;display:flex;align-items:center;justify-content:space-between}
.input--area{height:45px;align-items:flex-start;padding-top:6px}
.field-row{display:grid;grid-template-columns:1fr 1fr;gap:6px}
.input .dark{color:var(--ink)}
.btn-submit{height:20px;background:var(--espresso);color:var(--white);border-radius:10px;font-size:6px;font-weight:600;display:flex;align-items:center;justify-content:center;margin-top:3px}
.form-note{font-size:4.6px;color:var(--muted);text-align:center;margin-top:6px}

/* faq */
.page--faq .page-body{height:735px}
.faq-list{width:361px;margin:22px auto 0;display:flex;flex-direction:column;gap:6px}
.faq-item{background:var(--white);border-radius:5px;box-shadow:0 1px 5px rgba(60,30,20,.08);padding:0 12px 0 13px}
.faq-q{min-height:30px;display:flex;align-items:center;justify-content:space-between;font-size:6.1px;font-weight:600;letter-spacing:.2px;text-transform:uppercase;line-height:8.5px}
.faq-q span:first-child{max-width:250px}
.caret{color:var(--rose);font-size:6px}
.faq-a{font-size:6px;line-height:12.8px;color:var(--muted);padding:0 0 8px}
.faq-item--open .faq-q{min-height:27px}
.faq-item--tall .faq-q{min-height:35px}

/* footer */
.site-footer{background:var(--espresso);height:154px;padding:24px 45px 0;position:relative;color:var(--footer-text)}
.footer-grid{display:grid;grid-template-columns:178px 98px 98px 1fr}
.footer-brand{font-family:"Playfair Display",Georgia,serif;font-size:11px;line-height:12px;color:#f4ebe5;margin:4px 0 0 4px;white-space:nowrap}
.footer-about{font-size:6px;line-height:11px;color:#d9c8bf;margin-top:10px;max-width:140px}
.footer-col h5{font-size:6.3px;font-weight:600;color:var(--white);margin-bottom:8px}
.footer-col li{list-style:none;font-size:5.5px;line-height:13.4px}
.contact li{display:flex;align-items:flex-start;gap:5px;line-height:8px;margin-bottom:5.5px}
.contact svg{width:7px;height:7px;flex:none;margin-top:.5px}
.footer-bottom{position:absolute;left:45px;right:45px;top:119px;border-top:1px solid rgba(255,255,255,.08);padding-top:12px;display:flex;justify-content:space-between;font-size:5px;color:#8f7a6f}
</style>
</head>
<body>
<div class="stage">

  <section class="page page--designers">
    <header class="site-header">
      <div class="brand">The Gown Parlor of Ashcombe</div>
      <nav class="nav"><a>Home</a><a>About</a><a>What We Offer</a><a class="is-active">Designers</a><a>Appointments</a><a>FAQ</a><span class="btn-book">Book Now</span></nav>
    </header>
    <main class="page-body">
      <h1 class="page-title">Our Designers</h1>
      <p class="page-lead">We're proud to carry an exquisite roster of designers who share our commitment to beauty, quality, and craftsmanship.</p>
      <div class="designer-grid">
        <div class="designer-card"><span class="designer-name">Juniper Lane</span><span class="designer-type">Bridal</span></div>
        <div class="designer-card"><span class="designer-name">Moravia</span><span class="designer-type">Bridal</span></div>
        <div class="designer-card"><span class="designer-name">Tessa Olin</span><span class="designer-type">Bridal</span></div>
        <div class="designer-card"><span class="designer-name">Evermore Bridal Collection</span><span class="designer-type">Bridal</span></div>
        <div class="designer-card"><span class="designer-name">Dahlia Collection</span><span class="designer-type">Bridesmaid</span></div>
        <div class="designer-card"><span class="designer-name">Arden Sloane</span><span class="designer-type">Bridesmaid</span></div>
        <div class="designer-card"><span class="designer-name">Velmont Attire</span><span class="designer-type">Bridesmaid</span></div>
        <div class="designer-card"><span class="designer-name">Lovely Maidens</span><span class="designer-type">Bridesmaid</span></div>
        <div class="designer-card"><span class="designer-name">Maren Grey</span><span class="designer-type">Mother of the Occasion</span></div>
        <div class="designer-card"><span class="designer-name">MARZANO</span><span class="designer-type">Formal</span></div>
        <div class="designer-card"><span class="designer-name">Jay's Formal Wear</span><span class="designer-type">Menswear</span></div>
        <div class="designer-card"><span class="designer-name">Milford's Formal Wear</span><span class="designer-type">Tuxedos</span></div>
      </div>
      <p class="designer-note">✦ And more arriving each season. Contact us for a full list of designers.</p>
    </main>
    <footer class="site-footer">
      <div class="footer-grid">
        <div><div class="footer-brand">The Gown Parlor of Ashcombe</div><p class="footer-about">The Gown Parlor of Ashcombe — where Southern grace meets modern love. We're here for every beautiful moment.</p></div>
        <div class="footer-col"><h5>Explore</h5><ul><li>Home</li><li>About Us</li><li>What We Offer</li><li>Designers</li><li>FAQ</li></ul></div>
        <div class="footer-col"><h5>Services</h5><ul><li>Book Appointment</li><li>Bridal Gowns</li><li>Prom &amp; Formal</li><li>Tuxedos &amp; Suits</li></ul></div>
        <div class="footer-col"><h5>Connect</h5><ul class="contact">
          <li><svg viewBox="0 0 10 10"><path d="M2 1l2 2-1 1.3c.6 1.2 1.5 2.1 2.7 2.7L7 6l2 2-1.2 1.2C4.5 9 1 5.5.8 2.2z" fill="none" stroke="#bba99f" stroke-width=".8"/></svg>555-014-2270</li>
          <li><svg viewBox="0 0 10 10"><rect x="1" y="2.2" width="8" height="5.6" fill="none" stroke="#bba99f" stroke-width=".8"/><path d="M1 2.4l4 3 4-3" fill="none" stroke="#bba99f" stroke-width=".8"/></svg>appointments@gownparlorashcombe.com</li>
          <li><svg viewBox="0 0 10 10"><path d="M5 9.2S2 6 2 4a3 3 0 016 0c0 2-3 5.2-3 5.2z" fill="none" stroke="#bba99f" stroke-width=".8"/><circle cx="5" cy="4" r="1" fill="none" stroke="#bba99f" stroke-width=".8"/></svg>410 Marsh Lane Suite 2 Ashcombe SC 29000</li>
        </ul></div>
      </div>
      <div class="footer-bottom"><span>© 2026 The Gown Parlor of Ashcombe. All rights reserved.</span><span>Designed with love in the Lowcountry.</span></div>
    </footer>
  </section>

  <section class="page page--appointments">
    <header class="site-header">
      <div class="brand">The Gown Parlor of Ashcombe</div>
      <nav class="nav"><a>Home</a><a>About</a><a>What We Offer</a><a>Designers</a><a class="is-active">Appointments</a><a>FAQ</a><span class="btn-book">Book Now</span></nav>
    </header>
    <main class="page-body">
      <h1 class="page-title">Book Your Appointment</h1>
      <p class="page-lead">We'd love to welcome you to The Gown Parlor. Schedule a private, one-on-one styling session at your convenience.</p>
      <h2 class="section-title experience-heading">Choose Your Experience</h2>
      <div class="experience-grid">
        <article class="experience-card">
          <div class="experience-name">VIP Bridal Appointment <span class="badge">Exclusive</span></div>
          <div class="experience-meta">2 hours · Up to 10 guests</div>
          <p class="experience-desc">Enjoy a fully private 2-hour VIP bridal appointment with exclusive access to our entire boutique and two dedicated bridal consultants. No other brides will be present, giving you and your guests a relaxed, intimate experience.</p>
          <div class="vip-box">
            <h4>Your VIP experience includes:</h4>
            <ul class="vip-list">
              <li>Entire boutique reserved exclusively for you and your guests</li>
              <li>Two dedicated bridal consultants for your appointment</li>
              <li>Up to 10 guests</li>
              <li>Unlimited champagne</li>
              <li>Sweet treats and refreshments</li>
              <li>Charcuterie board</li>
              <li>Curated personal music mix</li>
              <li>Bridal emergency kit</li>
              <li>Bride gift bag including: Bride robe, lip balm, cup, slippers, bath bomb</li>
              <li>$50 off a wedding gown preservation kit</li>
            </ul>
          </div>
          <div class="fee"><b>Investment: $350</b> <span>· $250 credited back to gown purchase</span></div>
          <p class="fine-print">Availability: Currently offered on Sundays only. To request another day, email appointments@gownparlorashcombe.com.<br>Cancellation policy: Must provide at least 12 days' notice to avoid forfeiting the appointment fee.</p>
        </article>
        <article class="experience-card">
          <div class="experience-name">Bridal Appointment</div>
          <div class="experience-meta">1.5 hours · Up to 4 guests</div>
          <p class="experience-desc">Your 1.5-hour bridal appointment is a personalized, semi-private, one-on-one experience with an expert stylist dedicated to helping you find the one. Your stylist will learn about your wedding day, budget, and gown must-haves.</p>
          <p class="experience-desc">A $30 appointment fee is required to hold your time slot and is non-refundable upon cancellation.</p>
          <span class="fee">Fee: $30</span>
        </article>
        <article class="experience-card">
          <div class="experience-name">Find My Style</div>
          <div class="experience-meta">1 hour · Up to 4 guests</div>
          <p class="experience-desc">Not sure what style you're looking for? This self-guided experience lets you browse our curated selection at your own pace. A fitting area is reserved exclusively for you.</p>
          <span class="fee">Fee: $20 (non-refundable)</span>
        </article>
        <article class="experience-card">
          <div class="experience-name">Mothers Appointment</div>
          <div class="experience-meta">1 hour · Up to 4 guests</div>
          <p class="experience-desc">Dedicated time for mothers of the bride or groom to find elegant, sophisticated dresses for the special day.</p>
          <span class="fee">No fee</span>
        </article>
        <article class="experience-card">
          <div class="experience-name">Tuxedo / Suit Appointment</div>
          <div class="experience-meta">30 minutes · Up to 2 guests</div>
          <p class="experience-desc">Find the perfect formalwear for the groom, groomsmen, or fathers. We offer both rentals and purchases.</p>
          <span class="fee">No fee</span>
        </article>
        <article class="experience-card">
          <div class="experience-name">Bridesmaid Appointment</div>
          <div class="experience-meta">1 hour · Up to 6 guests</div>
          <p class="experience-desc">Coordinate your bridal party's look with a dedicated consultant to help find dresses that suit every style and body type.</p>
          <span class="fee">No fee</span>
        </article>
        <article class="experience-card">
          <div class="experience-name">Formal Wear Appointment</div>
          <div class="experience-meta">1 hour · Up to 4 guests</div>
          <p class="experience-desc">For any formal occasion — galas, charity events, black-tie affairs — we have the perfect ensemble.</p>
          <span class="fee">No fee</span>
        </article>
        <article class="experience-card">
          <div class="experience-name">Prom Appointment</div>
          <div class="experience-meta">1 hour · Up to 4 guests</div>
          <p class="experience-desc">Find a stunning prom dress that will make you feel like a star on your big night.</p>
          <span class="fee">No fee</span>
        </article>
      </div>

      <h2 class="section-title request-heading">Request an Appointment</h2>
      <p class="request-lead">We always welcome walk-ins, but to ensure a consultant is available, we recommend requesting an appointment. Select a type, date, and time below.</p>
      <div class="request-layout">
        <div class="experience-awaits">
          <h3>Your Experience Awaits</h3>
          <p>At The Gown Parlor, every appointment is designed to be as special as the occasion itself. We offer a relaxed, no-pressure environment where you can explore our collections with the undivided attention of a dedicated stylist.</p>
          <ul class="perks">
            <li>Private, one-on-one styling</li>
            <li>Access to our full designer collection</li>
            <li>Expert guidance on silhouettes, fabrics, and fit</li>
            <li>Refreshments and a warm, welcoming atmosphere</li>
            <li>Flexible scheduling — including evenings and weekends</li>
          </ul>
          <div class="callout"><b>Complimentary consultation</b> — no obligation, just beautiful dresses and genuine care.</div>
        </div>
        <form class="request-form">
          <h4>Request Your Visit</h4>
          <div class="field"><label>Full Name</label><div class="input">e.g. Sarah Elizabeth</div></div>
          <div class="field"><label>Email Address</label><div class="input">sarah@email.com</div></div>
          <div class="field"><label>Phone Number</label><div class="input">(555) 555-0123</div></div>
          <div class="field-row">
            <div class="field"><label>Preferred Date</label><div class="input"><span class="dark">08 / 26 / 2026</span><span class="dark">▭</span></div></div>
            <div class="field"><label>Preferred Time</label><div class="input"><span class="dark">Select a time</span><span class="dark">⌄</span></div></div>
          </div>
          <div class="field"><label>Appointment Type</label><div class="input"><span class="dark">Select one</span><span class="dark">⌄</span></div></div>
          <div class="field"><label>Anything else we should know?</label><div class="input input--area">Tell us about your vision, occasion, or any special requests...</div></div>
          <div class="btn-submit">Request Appointment</div>
          <p class="form-note">We'll respond within 24 hours to confirm your visit.</p>
        </form>
      </div>
    </main>
    <footer class="site-footer">
      <div class="footer-grid">
        <div><div class="footer-brand">The Gown Parlor of Ashcombe</div><p class="footer-about">The Gown Parlor of Ashcombe — where Southern grace meets modern love. We're here for every beautiful moment.</p></div>
        <div class="footer-col"><h5>Explore</h5><ul><li>Home</li><li>About Us</li><li>What We Offer</li><li>Designers</li><li>FAQ</li></ul></div>
        <div class="footer-col"><h5>Services</h5><ul><li>Book Appointment</li><li>Bridal Gowns</li><li>Prom &amp; Formal</li><li>Tuxedos &amp; Suits</li></ul></div>
        <div class="footer-col"><h5>Connect</h5><ul class="contact">
          <li><svg viewBox="0 0 10 10"><path d="M2 1l2 2-1 1.3c.6 1.2 1.5 2.1 2.7 2.7L7 6l2 2-1.2 1.2C4.5 9 1 5.5.8 2.2z" fill="none" stroke="#bba99f" stroke-width=".8"/></svg>555-014-2270</li>
          <li><svg viewBox="0 0 10 10"><rect x="1" y="2.2" width="8" height="5.6" fill="none" stroke="#bba99f" stroke-width=".8"/><path d="M1 2.4l4 3 4-3" fill="none" stroke="#bba99f" stroke-width=".8"/></svg>appointments@gownparlorashcombe.com</li>
          <li><svg viewBox="0 0 10 10"><path d="M5 9.2S2 6 2 4a3 3 0 016 0c0 2-3 5.2-3 5.2z" fill="none" stroke="#bba99f" stroke-width=".8"/><circle cx="5" cy="4" r="1" fill="none" stroke="#bba99f" stroke-width=".8"/></svg>410 Marsh Lane Suite 2 Ashcombe SC 29000</li>
        </ul></div>
      </div>
      <div class="footer-bottom"><span>© 2026 The Gown Parlor of Ashcombe. All rights reserved.</span><span>Designed with love in the Lowcountry.</span></div>
    </footer>
  </section>

  <section class="page page--faq">
    <header class="site-header">
      <div class="brand">The Gown Parlor of Ashcombe</div>
      <nav class="nav"><a>Home</a><a>About</a><a>What We Offer</a><a>Designers</a><a>Appointments</a><a class="is-active">FAQ</a><span class="btn-book">Book Now</span></nav>
    </header>
    <main class="page-body">
      <h1 class="page-title">Frequently Asked Questions</h1>
      <p class="page-lead" style="max-width:420px">Everything you need to know before your visit to The Gown Parlor of Ashcombe.</p>
      <div class="faq-list">
        <div class="faq-item faq-item--open">
          <div class="faq-q"><span>Do I need an appointment?</span><span class="caret">▲</span></div>
          <p class="faq-a">We encourage appointments so it allows us to cater to one bridal party at a time, ensuring that you receive our undivided attention as you find your dream gown and bridesmaid's dresses. Walk-ins are always welcomed and we will do our best to assist you! We understand our store hours may not fit your work hours. If you need an appointment after hours, please contact us directly.</p>
        </div>
        <div class="faq-item"><div class="faq-q"><span>How long do appointments last?</span><span class="caret">▼</span></div></div>
        <div class="faq-item"><div class="faq-q"><span>What should I bring to my appointment?</span><span class="caret">▼</span></div></div>
        <div class="faq-item"><div class="faq-q"><span>What size are your sample gowns?</span><span class="caret">▼</span></div></div>
        <div class="faq-item"><div class="faq-q"><span>What is the price range of your gowns?</span><span class="caret">▼</span></div></div>
        <div class="faq-item"><div class="faq-q"><span>When should I start dress shopping?</span><span class="caret">▼</span></div></div>
        <div class="faq-item"><div class="faq-q"><span>When will my gown arrive?</span><span class="caret">▼</span></div></div>
        <div class="faq-item"><div class="faq-q"><span>How do I know what size to order?</span><span class="caret">▼</span></div></div>
        <div class="faq-item"><div class="faq-q"><span>Do you offer alterations?</span><span class="caret">▼</span></div></div>
        <div class="faq-item"><div class="faq-q"><span>Do you offer shipping?</span><span class="caret">▼</span></div></div>
        <div class="faq-item"><div class="faq-q"><span>What are your payment options?</span><span class="caret">▼</span></div></div>
        <div class="faq-item"><div class="faq-q"><span>Who should I bring to my appointment?</span><span class="caret">▼</span></div></div>
        <div class="faq-item"><div class="faq-q"><span>Do you offer formal wear for the guys?</span><span class="caret">▼</span></div></div>
        <div class="faq-item faq-item--tall"><div class="faq-q"><span>Will the other groomsmen have to set up an appointment for measurements?</span><span class="caret">▼</span></div></div>
        <div class="faq-item"><div class="faq-q"><span>Can you ship men's formal wear?</span><span class="caret">▼</span></div></div>
      </div>
    </main>
    <footer class="site-footer">
      <div class="footer-grid">
        <div><div class="footer-brand">The Gown Parlor of Ashcombe</div><p class="footer-about">The Gown Parlor of Ashcombe — where Southern grace meets modern love. We're here for every beautiful moment.</p></div>
        <div class="footer-col"><h5>Explore</h5><ul><li>Home</li><li>About Us</li><li>What We Offer</li><li>Designers</li><li>FAQ</li></ul></div>
        <div class="footer-col"><h5>Services</h5><ul><li>Book Appointment</li><li>Bridal Gowns</li><li>Prom &amp; Formal</li><li>Tuxedos &amp; Suits</li></ul></div>
        <div class="footer-col"><h5>Connect</h5><ul class="contact">
          <li><svg viewBox="0 0 10 10"><path d="M2 1l2 2-1 1.3c.6 1.2 1.5 2.1 2.7 2.7L7 6l2 2-1.2 1.2C4.5 9 1 5.5.8 2.2z" fill="none" stroke="#bba99f" stroke-width=".8"/></svg>555-014-2270</li>
          <li><svg viewBox="0 0 10 10"><rect x="1" y="2.2" width="8" height="5.6" fill="none" stroke="#bba99f" stroke-width=".8"/><path d="M1 2.4l4 3 4-3" fill="none" stroke="#bba99f" stroke-width=".8"/></svg>appointments@gownparlorashcombe.com</li>
          <li><svg viewBox="0 0 10 10"><path d="M5 9.2S2 6 2 4a3 3 0 016 0c0 2-3 5.2-3 5.2z" fill="none" stroke="#bba99f" stroke-width=".8"/><circle cx="5" cy="4" r="1" fill="none" stroke="#bba99f" stroke-width=".8"/></svg>410 Marsh Lane Suite 2 Ashcombe SC 29000</li>
        </ul></div>
      </div>
      <div class="footer-bottom"><span>© 2026 The Gown Parlor of Ashcombe. All rights reserved.</span><span>Designed with love in the Lowcountry.</span></div>
    </footer>
  </section>

</div>
</body>
</html>
```